Company business card

We need a new business card design. We are IT company which is specialized for outsourcing of operations hardware and software (specially Quorvane, we are a partner), developing custom applications and web applications, BPM solutions, auditing hw and sw. actually design was attached. But we need completely NEW.

Business

```html
<!DOCTYPE html>
<html lang="sk">
<head>
<meta charset="utf-8">
<title>Velnor – vizitka</title>
<link rel="stylesheet" href="https://fonts.googleapis.com/css2?family=Montserrat:wght@700&family=Source+Sans+3:wght@400;600;700&display=swap">
<style>
  :root {
    --backdrop: #8a8b8b;
    --card-white: #ececec;
    --brand-blue: #1f74bd;
    --ink-dark: #2e2f30;
    --ink-text: #3d3e40;
    --ink-muted: #4a4b4d;
  }
  html, body { margin: 0; padding: 0; }
  body {
    width: 1200px; height: 900px; overflow: hidden;
    background: var(--backdrop);
    position: relative;
    font-family: "Source Sans 3", sans-serif;
  }
  .card {
    position: absolute; left: 321px;
    width: 507px; height: 290px;
    background: var(--card-white);
    box-shadow: 0 10px 18px rgba(0,0,0,.28);
    overflow: hidden;
  }
  .card--front { top: 119px; }
  .card--back  { top: 471px; }

  .brand { position: absolute; display: flex; align-items: center; gap: 14px; }
  .brand__square { width: 74px; height: 74px; }
  .brand__name {
    font-family: "Montserrat", sans-serif; font-weight: 700;
    font-size: 44px; line-height: 40px; letter-spacing: -0.5px;
  }
  .card--front .brand { left: 163px; top: 108px; }
  .card--front .brand__square { background: var(--brand-blue); }
  .card--front .brand__name { color: var(--ink-dark); }

  .front__web {
    position: absolute; left: 0; right: 0; top: 253px;
    text-align: center; font-size: 13px; letter-spacing: 5px;
    color: var(--ink-muted);
  }

  .back__band { position: absolute; inset: 0; }
  .card--back .brand { left: 287px; top: 107px; }
  .card--back .brand__square { background: #fff; width: 75px; height: 75px; }
  .card--back .brand__name { color: #fff; }

  .contact { position: absolute; left: 43px; top: 67px; color: var(--ink-text); }
  .contact__name { font-size: 19px; font-weight: 700; color: var(--brand-blue); margin: 0; line-height: 22px; }
  .contact__role { font-size: 14px; margin: 1px 0 10px; }
  .contact__address { font-size: 12.5px; line-height: 15.5px; margin: 0 0 8px; font-style: normal; }
  .contact__list { list-style: none; margin: 0; padding: 0; font-size: 12.5px; }
  .contact__list li { display: flex; align-items: center; gap: 7px; height: 19.5px; }
  .contact__icon { width: 13px; height: 13px; flex: none; }
</style>
</head>
<body>

<section class="card card--front" aria-label="Predná strana vizitky">
  <div class="brand">
    <div class="brand__square"></div>
    <div class="brand__name">VEL<br>NOR</div>
  </div>
  <div class="front__web">www.velnor.sk</div>
</section>

<section class="card card--back" aria-label="Zadná strana vizitky">
  <svg class="back__band" viewBox="0 0 507 290" width="507" height="290" aria-hidden="true">
    <polygon points="143,0 507,0 507,290 141,290 281,145" fill="var(--brand-blue)"/>
  </svg>

  <div class="contact">
    <h1 class="contact__name">Marek Dolinský</h1>
    <div class="contact__role">CEO</div>
    <address class="contact__address">Velnor s.r.o.<br>Lipová 12<br>811 02 Bratislava</address>
    <ul class="contact__list">
      <li>
        <svg class="contact__icon" viewBox="0 0 13 13" aria-hidden="true">
          <rect x="3" y="0.5" width="7" height="12" rx="1.2" fill="none" stroke="var(--brand-blue)" stroke-width="1.4"/>
          <rect x="4.5" y="2.2" width="4" height="7" fill="var(--brand-blue)"/>
        </svg>+421 (0) 900 123 456
      </li>
      <li>
        <svg class="contact__icon" viewBox="0 0 13 13" aria-hidden="true">
          <rect x="0.5" y="2.5" width="12" height="8" fill="var(--brand-blue)"/>
          <polyline points="0.5,2.5 6.5,7 12.5,2.5" fill="none" stroke="#fff" stroke-width="1"/>
        </svg>marek.dolinsky@velnor.sk
      </li>
      <li>
        <svg class="contact__icon" viewBox="0 0 13 13" aria-hidden="true">
          <circle cx="6.5" cy="6.5" r="6" fill="var(--brand-blue)"/>
          <ellipse cx="6.5" cy="6.5" rx="2.6" ry="6" fill="none" stroke="#fff" stroke-width="0.8"/>
          <line x1="0.5" y1="6.5" x2="12.5" y2="6.5" stroke="#fff" stroke-width="0.8"/>
        </svg>www.velnor.sk
      </li>
    </ul>
  </div>

  <div class="brand">
    <div class="brand__square"></div>
    <div class="brand__name">VEL<br>NOR</div>
  </div>
</section>

</body>
</html>
```